Bright Harbor Health (03)

We're designing a website to sell Medicare Supplements. Attached is the script we want to say and general layout, but please use your best knowledge to make it better. This platform should be extremely user-friendly, but we want to make it look fun and approachable! Most Insurance/medicare websites are very boring, drab, simple but we want this one to be more personalized, fun and sexy (but again, still user-friendly since our target demographic is 65+).

This homepage should include a fun and inviting quiz, the script is in the attachment below. It should also include the blurbs about what medicare supplements plans are and why they should buy them. Feel free to play around with cool fonts and imagery, we want the site to be engaging!

Target Market(s)

seniors

Industry/Entity Type

Insurance

Number of Pages Required

1 page

Requirements
Must have
• Quiz, company name and tag line, script
Nice to have
• fun, engaging elements

```html
<!DOCTYPE html>
<html lang="en">
<head>
<meta charset="utf-8">
<title>Bright Harbor Health</title>
<link rel="stylesheet" href="https://fonts.googleapis.com/css2?family=Roboto:wght@400;500;700&display=swap">
<style>
  :root {
    --navy-deep: #0c2746;
    --navy: #123a63;
    --navy-mid: #1b4f7c;
    --ink: #1c2f5a;
    --green: #4cbc74;
    --green-soft: #a9d98c;
    --sky: #cfe9ff;
    --teal: #1d6d8f;
    --teal-dark: #154d6e;
    --grey-text: #555b61;
    --grey-line: #d9dcdf;
    --band: #a9b3bf;
    --white: #ffffff;
  }
  * { box-sizing: border-box; margin: 0; padding: 0; }
  html, body { width: 1200px; height: 1200px; overflow: hidden; background: var(--white); }
  body { font-family: "Roboto", Arial, sans-serif; position: relative; }

  .hero { position: absolute; left: 0; top: 0; width: 1200px; height: 570px; overflow: hidden; }
  .hero-photo {
    position: absolute; inset: 0;
    background:
      radial-gradient(ellipse 420px 320px at 420px 180px, rgba(70,110,150,0.55), transparent 70%),
      radial-gradient(ellipse 360px 300px at 980px 330px, rgba(60,100,140,0.5), transparent 70%),
      linear-gradient(180deg, var(--navy-deep) 0%, var(--navy) 55%, var(--navy-mid) 100%);
  }
  .hero-curve { position: absolute; left: 0; bottom: 0; width: 1200px; height: 70px; }

  .brand-title {
    position: absolute; top: 135px; left: 0; width: 1200px; text-align: center;
    color: var(--white); font-weight: 700; font-size: 72px; letter-spacing: -0.5px;
  }
  .tagline {
    position: absolute; top: 232px; left: 0; width: 1200px; text-align: center;
    color: var(--green-soft); font-weight: 700; font-size: 27px;
  }
  .divider-accent {
    position: absolute; top: 298px; left: 350px; width: 501px; height: 14px;
    background: var(--green); opacity: 0.35; border-radius: 2px;
  }
  .call-row { position: absolute; top: 328px; left: 154px; display: flex; align-items: center; }
  .call-icon { width: 106px; height: 106px; }
  .call-text { margin-left: 18px; font-size: 39px; font-weight: 500; color: var(--sky); }
  .call-text .phone { color: var(--green); }

  .intro {
    position: absolute; top: 626px; left: 100px; width: 1000px; text-align: center;
    color: var(--grey-text); font-weight: 500; font-size: 21px; line-height: 29px;
  }
  .intro-cta {
    position: absolute; top: 700px; left: 0; width: 1200px; text-align: center;
    color: var(--ink); font-weight: 700; font-size: 21px;
  }

  .quiz-card {
    position: absolute; top: 773px; left: 243px; width: 716px; height: 500px;
    border: 1.5px solid var(--grey-line); border-radius: 6px; background: var(--white);
    padding: 0 30px;
  }
  .quiz-question { padding: 26px 6px 30px; border-bottom: 1.5px solid var(--grey-line); }
  .quiz-question:last-child { border-bottom: none; }
  .quiz-label { font-size: 36px; color: var(--grey-text); font-weight: 400; margin-bottom: 20px; line-height: 46px; }
  .quiz-option { display: flex; align-items: center; font-size: 24px; color: var(--grey-text); height: 38.5px; }
  .quiz-radio {
    width: 13px; height: 13px; border: 1.5px solid var(--grey-text); border-radius: 50%;
    margin: 0 17px 0 4px;
  }
</style>
</head>
<body>
  <header class="hero">
    <div class="hero-photo" role="img" aria-label="Photograph of a smiling senior couple, toned in deep navy blue"></div>
    <svg class="hero-curve" viewBox="0 0 1200 70" preserveAspectRatio="none" aria-hidden="true">
      <path d="M0 40 L600 62 L1200 40 L1200 70 L0 70 Z" fill="var(--band)" opacity="0.6"/>
      <path d="M0 48 Q300 56 600 62 Q900 56 1200 48 L1200 70 L0 70 Z" fill="var(--band)" opacity="0.8"/>
      <path d="M0 60 L600 64 L1200 60 L1200 70 L0 70 Z" fill="var(--white)"/>
    </svg>

    <h1 class="brand-title">Bright Harbor Health</h1>
    <p class="tagline">Be confident in choosing the Medicare Supplement plan that’s right for you.</p>
    <div class="divider-accent" role="img" aria-label="Green hatched decorative divider"></div>

    <div class="call-row">
      <svg class="call-icon" viewBox="0 0 106 106" aria-hidden="true">
        <circle cx="53" cy="53" r="53" fill="var(--teal)"/>
        <circle cx="53" cy="53" r="37" fill="var(--teal-dark)"/>
        <path d="M41 37 C38 40 37 45 40 51 C44 59 50 65 57 69 C62 72 67 71 70 68 L66 62 C65 61 63 61 62 62 L59 64 C54 61 49 56 46 51 L48 48 C49 47 49 45 48 44 Z" fill="var(--sky)"/>
      </svg>
      <p class="call-text">Call <span class="phone">(800) 555-0147</span> to talk to a live agent</p>
    </div>
  </header>

  <main>
    <p class="intro">We know insurance can be confusing. With so much information and not enough answers, we’re here to help you find the plan that works best for you, your family and your health.</p>
    <p class="intro-cta">Take this short quiz to find flexible and affordable plans that you can feel confident in.</p>

    <div class="quiz-card">
      <div class="quiz-question">
        <p class="quiz-label">I am</p>
        <div class="quiz-option"><span class="quiz-radio"></span>Over 64 years old</div>
        <div class="quiz-option"><span class="quiz-radio"></span>64 years old</div>
        <div class="quiz-option"><span class="quiz-radio"></span>Under 64 years old</div>
      </div>
      <div class="quiz-question">
        <p class="quiz-label">I am</p>
        <div class="quiz-option"><span class="quiz-radio"></span>Male</div>
      </div>
    </div>
  </main>
</body>
</html>
```